Business Card Design Project

We are a consulting company which works with tourism operators and attractions, wineries, heritage sites, National and conservation parks etc to help them identify their 'Point of Difference' and then deliver an exceptional tourism visitor experience.
We specialise in: Guide Coaching, Visitor Storytelling, Destination and Visitor Development, Strategy and Research.
We have a tag line of "Sharing your place - truly well."
The company name is MoxVerse and the logo is this word with the 'Mox' in black and the 'Verse' in orange - but this can be changed. The 'a' is a speech bubble. A lot of what we do involves talking!
The design should communicate that we can make a big difference to the range and quality of experiences that visitors get at your site.
Updates

I put the wrong telephone number in my brief. My apologies.

It should be +61 0481 902 317

Target Market(s)

tourism busineses, wineries and cellar doors, heritage sites, environment managers, Government agencies & private companies

Industry/Entity Type

Tourism

Requirements
Must have
• Name: Corin Hollis
Title: Adjunct Professor
Qualifications: BA(Hons), MSc
Role: Director
Address: PO Box 318, Harbourne, Coastline SA 5177
Phone: (+61) 0481 902 317
Email: corin@moxverse-example.com.au
www.moxverse-example.com.au
ABN 871 204 519 36

Guide Coaching, Visitor Storytelling, Destination and Visitor Development, Strategy and Research.
Nice to have
• Awards:
Winner 2011 SA Voyager Honours – Kestrel Polytechnic - Tourism Education and Training
Winner 2009 SA Voyager Honours - Outstanding Contribution by an Individual
Winner 2009 Gulfland Citizen Medal - Tourism Award
Should not have
• No 'shadows' to company name/logo please.
No black reverse side of card

```html
<!DOCTYPE html>
<html lang="en">
<head>
<meta charset="utf-8">
<title>MoxVerse Consulting – Business Card</title>
<link rel="stylesheet" href="https://fonts.googleapis.com/css2?family=Ubuntu:wght@400;500;700&display=swap">
<style>
  :root {
    --orange: #ec7200;
    --ink: #1a1a1a;
    --grey: #5f5f5f;
    --text: #333333;
    --card: #ffffff;
    --backdrop: #3a3a3a;
  }
  * { margin: 0; padding: 0; box-sizing: border-box; }
  html, body { width: 1200px; height: 900px; overflow: hidden; }
  body {
    background: var(--backdrop);
    font-family: "Ubuntu", sans-serif;
    position: relative;
  }
  .card {
    position: absolute;
    top: 301px;
    width: 515px;
    height: 296px;
    background: var(--card);
    overflow: hidden;
  }
  .card--front { left: 72px; }
  .card--back { left: 615px; }

  /* Front */
  .front-wordmark {
    position: absolute;
    left: 0;
    right: 0;
    top: 52px;
    text-align: center;
    font-weight: 700;
    font-size: 108px;
    line-height: 1;
    letter-spacing: -2px;
    color: var(--orange);
  }
  .front-descriptor {
    position: absolute;
    right: 6px;
    top: 190px;
    font-weight: 500;
    font-size: 30px;
    line-height: 34px;
    letter-spacing: 5px;
    color: var(--grey);
  }
  .front-tagline {
    position: absolute;
    left: 131px;
    top: 256px;
    font-size: 17px;
    color: var(--orange);
  }

  /* Back */
  .contact {
    position: absolute;
    left: 43px;
    top: 86px;
    font-size: 11.5px;
    line-height: 15px;
    color: var(--text);
  }
  .contact__name {
    font-size: 19px;
    line-height: 22px;
    font-variant: small-caps;
    color: var(--orange);
    margin-bottom: 2px;
  }
  .contact__lines { margin-bottom: 14px; }
  .contact__label { color: var(--orange); }
  .back-logo {
    position: absolute;
    left: 236px;
    top: 34px;
    width: 200px;
    text-align: right;
  }
  .back-logo__name {
    font-weight: 700;
    font-size: 38px;
    line-height: 1;
    letter-spacing: -1px;
    color: var(--orange);
  }
  .back-logo__descriptor {
    font-weight: 500;
    font-size: 13px;
    letter-spacing: 2.5px;
    color: var(--grey);
    margin-top: 6px;
  }
  .abn {
    position: absolute;
    left: 478px;
    top: 35px;
    writing-mode: vertical-rl;
    transform: rotate(180deg);
    font-size: 7px;
    color: var(--text);
  }
  .services {
    position: absolute;
    left: 309px;
    top: 134px;
    list-style: none;
    font-weight: 500;
    font-size: 13.5px;
    line-height: 16px;
    color: var(--ink);
  }
  .services__item {
    position: relative;
    padding-left: 20px;
    margin-bottom: 15px;
  }
  .services__bullet {
    position: absolute;
    left: 0;
    top: 3px;
    width: 11px;
    height: 11px;
  }
</style>
</head>
<body>
  <section class="card card--front" aria-label="Card front">
    <div class="front-wordmark">MoxVerse</div>
    <div class="front-descriptor">CONSULTING</div>
    <p class="front-tagline">Sharing your place - truly well</p>
  </section>

  <section class="card card--back" aria-label="Card back">
    <div class="contact">
      <div class="contact__name">Corin Hollis</div>
      <div class="contact__lines">
        Adjunct Professor<br>
        BA(Hons), MSc<br>
        Director
      </div>
      <div class="contact__lines">
        <span class="contact__label">p :</span> +61 0481 902 317<br>
        <span class="contact__label">e :</span> corin@moxverse-example.com.au<br>
        <span class="contact__label">w:</span> www.moxverse-example.com.au
      </div>
      <div>
        PO Box 318, Harbourne<br>
        Coastline SA 5177
      </div>
    </div>

    <div class="back-logo">
      <div class="back-logo__name">MoxVerse</div>
      <div class="back-logo__descriptor">CONSULTING</div>
    </div>

    <div class="abn">ABN 871 204 519 36</div>

    <ul class="services">
      <li class="services__item"><svg class="services__bullet" viewBox="0 0 10 10"><circle cx="5" cy="5" r="5" fill="#ec7200"/></svg>Guide Coaching</li>
      <li class="services__item"><svg class="services__bullet" viewBox="0 0 10 10"><circle cx="5" cy="5" r="5" fill="#ec7200"/></svg>Visitor Storytelling</li>
      <li class="services__item"><svg class="services__bullet" viewBox="0 0 10 10"><circle cx="5" cy="5" r="5" fill="#ec7200"/></svg>Destination and Visitor<br>Development</li>
      <li class="services__item"><svg class="services__bullet" viewBox="0 0 10 10"><circle cx="5" cy="5" r="5" fill="#ec7200"/></svg>Strategy and Research</li>
    </ul>
  </section>
</body>
</html>
```